Coffee ecommerce website design

We are re-branding our website, starting with the logo which has now been done (see uploaded files).

Our website sells coffee and coffee-related products and accessories, with the vast majority of products not available in the supermarket or coffee shop - these brands are known, just not widely available in the UK. Our customers either know the product or brand because they have tried it somewhere (abroad), know of it (for example, if they are Italian) or they want to try something different.

The website has to be clean and simple (currently it is too cluttered) and make it easy to promote products. At the same time, not too simple that it looks cheap. Of course we don't claim to be anything like these, but to give you an idea, this is what we mean by clean, simple, professional ecommerce:
- http://www.harrowfield.example/home-garden/c500006
- http://www.pellwarmarket.example
- http://www.quillandcrest.example
- http://www.vortellishop.example
- http://www.52harbour.example

Currently we are only looking for the design work - development can be discussed at a later date if you like.

Please take any assets such as images, text, etc. from our current website.

If you require any further information, please do ask. We would like to see the home page, category page and product page.

Many thanks,
Updates

Hi, we've seen some great designs so far - it will help to also see some product pages. Thanks.

Target Market(s)

Predominantly men and women between 35 and 60, descent income who enjoy good quality food and drink. The majority know their coffee, and are fussy about the coffee they drink.

Requirements
Must have
• Font - modern and maybe different, like Open Sans, Bree, Source Sans Pro.
• Strips/boxes where we can promote free delivery over £60, our loyalty points, quick turnaround, etc. Look at the top of our current website http://www.brewcellarhub.example or underneath the menu bar of http://www.52harbour.example (we like this simplicity and cleanliness by the way).
• Sorry if the following sounds obvious, but just to clarify, we would need the home page to have following (always following the route of cleanliness and simplicity...):
• - Menu//navigation bar
• - Search box
• - Telephone number
• - SSL seal (see side of current website)
• - Payment methods (we don't need all the card logos to be shown, just some sort of reference to PayNimbus, Vextora and Credit/Debit Cards)
• - Social media icons for Chatterly, chirpwave, clipstream, Snapframe, vextora+ and Boardnook
• - Selected products on the home page like we currently have under the HOT PRODUCTS section (see below, as we are looking to change this title to NEW ARRIVALS).
• - Coupon request by email box as per current site
• - Product rating icons (currently stars, but these can be unique/different)
• - Paragraph(s) of text for around 200 words
• - Cart value icon (have a look at http:.//www.tazlorno.example and see the red circle)
• - Carousel
• For the product page, the page must feature:
• - Product Title, quantity box, price, add to cart, availability, item reviews, product description (between 100 and 200 words, in paragraph and bullet points)
• - Product options (size, colour)
• - Social media share icons (Chatterly, chirpwave and Boardnook only)
• - Cross selling (Similar items)
• - Up-selling (buy these 2 items together and save xx%)
• - One this we will be adding is filtering by attribute, so for example, http://www.gwbrackett.example/All-Suits/Mens-Suit-Bundles,en_GB,sc.html where you can select colour, size, etc.
Nice to have
• If you can make it work, we'd like a NEW ARRIVALS/NEWEST PRODUCTS/JUST IN products area (on our current site we have HOT PRODUCTS for example).
• We want to promote the brands we sell by showing the logos, such as http://www.swiftbeanpost.example (but not scrolling).
• Our strategy includes creating videos for some products, so somewhere on the product page we would like to have a ClipStream video embedded.

```html
<!DOCTYPE html>
<html lang="en">
<head>
<meta charset="utf-8">
<title>brewcellarhub – Buy fresh coffee</title>
<link rel="stylesheet" href="https://fonts.googleapis.com/css2?family=Open+Sans:wght@300;400;600;700;800&display=swap">
<style>
:root{
  --red:#f03c14;
  --red-dark:#d9310d;
  --ink:#3a3a3a;
  --muted:#8a8a8a;
  --line:#e2e2e2;
  --ring:#e6e6e6;
  --panel:#f4f4f4;
  --white:#ffffff;
}
*{box-sizing:border-box;margin:0;padding:0}
html,body{width:1200px;height:2851px;overflow:hidden}
body{position:relative;background:var(--white);font-family:"Open Sans",Arial,sans-serif;color:var(--ink)}
.abs{position:absolute}

/* top bar */
.topbar{left:0;top:0;width:1200px;height:46px;border-bottom:1px solid var(--line)}
.social-mini{left:216px;top:12px;display:flex;gap:5px}
.social-mini span{width:18px;height:18px;border-radius:50%;border:2px solid var(--red);display:block}
.search{left:308px;top:12px;width:228px;height:18px;border:1px solid #d6d6d6;border-radius:9px}
.search svg{position:absolute;right:6px;top:3px}
.account-links{left:582px;top:14px;font-size:9px;font-weight:700;letter-spacing:.3px;display:flex;gap:10px;text-transform:uppercase}
.account-links .hello{color:var(--red)}
.cart{left:880px;top:0;width:118px;height:46px;border-left:1px solid var(--line);border-right:1px solid var(--line);padding:7px 0 0 14px}
.cart .total{font-size:17px;font-weight:700;color:var(--ink);line-height:18px}
.cart .total small{font-size:8px;font-weight:600}
.cart .items{font-size:7px;color:var(--red);font-weight:700}
.cart svg{position:absolute;right:10px;top:14px}

/* header */
.logo{left:216px;top:64px;display:flex;align-items:center;gap:10px}
.logo .mark{width:56px;height:56px;border-radius:50%;background:var(--red)}
.logo .name{font-size:19px;font-weight:700;color:var(--ink)}
.mainnav{left:520px;top:86px;display:flex;gap:34px;font-size:11px;font-weight:700;letter-spacing:1px;color:var(--red);text-transform:uppercase}

/* hero */
.hero{left:0;top:154px;width:1200px;height:495px;background:linear-gradient(100deg,#d9c1a6 0%,#c8a78a 22%,#e9e3dc 45%,#a98c74 70%,#7a6552 100%)}
.hero-copy{right:182px;top:266px;text-align:right;color:var(--white)}
.hero-copy .kicker{font-size:12px;font-weight:700;color:var(--red);text-transform:uppercase;letter-spacing:.5px}
.hero-copy h1{font-size:44px;font-weight:300;line-height:42px;text-transform:uppercase;margin-top:4px}
.hero-copy p{font-size:19px;font-weight:700;line-height:21px}
.hero-copy .more{font-size:6px;font-weight:700;margin-top:16px;text-transform:uppercase}
.dots{left:568px;top:622px;display:flex;gap:6px}
.dots span{width:14px;height:14px;border-radius:50%;background:#8d8d8d}
.dots span.on{background:var(--red)}

/* intro */
.intro{left:0;top:649px;width:1200px;height:330px;background:var(--panel)}
.intro h2{position:absolute;left:0;width:1200px;top:64px;text-align:center;font-size:19px;font-weight:700;color:var(--red)}
.intro-text{position:absolute;left:300px;top:108px;width:600px;font-size:10.5px;line-height:15px;color:#555}
.intro-text p{margin-bottom:12px}
.intro-text em{font-style:normal;color:var(--red);font-weight:600}

/* section banners */
.pill{left:385px;width:430px;height:38px;border-radius:19px;background:var(--red);color:var(--white);font-size:13px;font-weight:700;letter-spacing:1.5px;text-align:center;line-height:38px;text-transform:uppercase;box-shadow:0 6px 10px rgba(0,0,0,.08)}
.rule-title{left:270px;width:660px;display:flex;align-items:center;gap:14px;font-size:13px;font-weight:700;letter-spacing:1.5px;color:var(--red);text-transform:uppercase}
.rule-title::before,.rule-title::after{content:"";flex:1;height:1px;background:var(--line)}

/* products */
.row{left:292px;width:616px;display:flex;justify-content:space-between}
.product{width:176px;text-align:center;position:relative}
.product .ring{width:176px;height:176px;border-radius:50%;border:7px solid var(--ring);background:var(--white);display:flex;align-items:center;justify-content:center;position:relative;overflow:hidden}
.product .ring.active{border-color:var(--red)}
.product .shot{width:72px;height:108px;border-radius:8px}
.product .flag{position:absolute;left:0;right:0;bottom:18px;background:#2b2b2b;color:var(--white);font-size:8px;font-weight:700;line-height:12px;padding:3px 0;text-transform:uppercase}
.product .compare{font-size:8px;font-weight:700;letter-spacing:1.2px;margin-top:10px;color:#555}
.product .buy{display:inline-block;margin-top:3px;padding:2px 12px;border-radius:8px;background:#dcdcdc;font-size:8px;font-weight:700;letter-spacing:1.2px;color:#555}
.product .badge{position:absolute;left:-4px;top:-2px;width:38px;height:38px;border-radius:50%;background:var(--red);color:var(--white);font-size:10px;font-weight:800;line-height:38px;z-index:2}

/* help panel */
.help{left:200px;top:1972px;width:800px;height:653px;background:var(--panel)}
.columns{left:238px;top:2055px;width:760px;display:flex}
.col{width:253px;padding-right:26px;border-right:1px solid var(--line);padding-left:0}
.col+.col{padding-left:26px}
.col:last-child{border-right:none}
.col-head{display:flex;gap:10px;align-items:flex-start}
.col-head h3{font-size:17px;line-height:17px;font-weight:700;color:var(--red)}
.col p{font-size:9px;line-height:13px;color:#666;margin-top:12px}
.col .read{display:block;text-align:center;font-size:7px;font-weight:700;letter-spacing:.8px;margin-top:20px;text-transform:uppercase}

.delivery{left:238px;top:2428px;width:760px;display:flex;justify-content:space-between}
.delivery .block{width:240px}
.delivery h3{font-size:19px;line-height:19px;font-weight:700;color:var(--red)}
.delivery p{font-size:9px;line-height:13px;color:#666;margin-top:10px}
.courier{width:168px;height:168px;border-radius:50%;border:7px solid var(--red);background:radial-gradient(circle at 50% 40%,#9fb4c6 0%,#5b7183 45%,#c9a57a 80%);margin-top:0}
.cards{display:grid;grid-template-columns:repeat(3,52px);gap:5px;margin:14px 0 0 44px}
.cards span{height:28px;border:1px solid #cfcfcf;border-radius:3px;background:var(--white);font-size:8px;font-weight:700;line-height:26px;text-align:center;color:#444}

/* footer */
.foot-logo{left:216px;top:2645px;display:flex;align-items:center;gap:6px}
.foot-logo .mark{width:24px;height:24px;border-radius:50%;background:var(--red)}
.foot-logo .name{font-size:15px;font-weight:700}
.foot-cols{left:470px;top:2643px;display:flex;gap:0}
.foot-cols div{width:134px}
.foot-cols h4{font-size:7px;font-weight:700;color:var(--red);letter-spacing:.8px;text-transform:uppercase;margin-bottom:4px}
.foot-cols li{list-style:none;font-size:6.5px;line-height:9px;letter-spacing:.6px;color:#666;text-transform:uppercase}
.join{left:470px;top:2732px;font-size:7px;font-weight:700;color:var(--red);letter-spacing:.8px}
.join-icons{left:466px;top:2750px;display:flex;gap:6px}
.join-icons span{width:22px;height:22px;border-radius:50%;background:var(--red);display:block}
.seal{left:928px;top:2756px;width:52px;height:30px;border-radius:4px;background:#cfd6c8}
.copy{left:216px;top:2828px;font-size:6px;font-weight:600;letter-spacing:1px;color:var(--white);text-transform:uppercase;z-index:2}
.strip{left:200px;top:2818px;width:800px;height:33px;background:var(--red)}
</style>
</head>
<body>

<!-- top bar -->
<div class="abs topbar"></div>
<div class="abs social-mini" aria-label="Chatterly, chirpwave, clipstream and vextora+ links"><span></span><span></span><span></span><span></span></div>
<div class="abs search">
  <svg width="10" height="10" viewBox="0 0 10 10"><circle cx="4" cy="4" r="3" fill="none" stroke="#aaa" stroke-width="1.2"/><line x1="6.2" y1="6.2" x2="9" y2="9" stroke="#aaa" stroke-width="1.2"/></svg>
</div>
<nav class="abs account-links"><span class="hello">Hello Alex Marlow</span><span>Gift list</span><span>My account</span><span>Logout</span></nav>
<div class="abs cart">
  <div class="total">£72.3 <small>(3 items)</small></div>
  <div class="items">Checkout</div>
  <svg width="26" height="20" viewBox="0 0 26 20"><path d="M1 6h24l-3 12H4z" fill="var(--red)"/><path d="M8 6l4-5M18 6l-4-5" stroke="var(--red)" stroke-width="2" fill="none"/></svg>
</div>

<!-- header -->
<a class="abs logo"><span class="mark"></span><span class="name">brewcellarhub</span></a>
<nav class="abs mainnav"><span>Coffee</span><span>Machines</span><span>Accessories</span><span>Other drinks</span><span>Goodies</span></nav>

<!-- hero carousel -->
<div class="abs hero" role="img" aria-label="Photo of a woman sipping from a white cup"></div>
<div class="abs hero-copy">
  <div class="kicker">Hot drinks</div>
  <h1>Drinking<br>pleasure</h1>
  <p>The most luxurious drinks<br>for any time of your day</p>
  <div class="more">Discover more here</div>
</div>
<div class="abs dots"><span class="on"></span><span></span><span></span></div>

<!-- intro -->
<section class="abs intro">
  <h2>Buy fresh coffee from brewcellarhub</h2>
  <div class="intro-text">
    <p>Since 2009 we have served customers throughout the UK, Ireland, and mainland Europe, giving customers who buy their coffee online the confidence their order of fresh coffee will be received quickly and easily. Our <em>delivery rates</em> are competitive, starting at <em>just £3.99</em>, and we have low delivery prices for coffee lovers who buy from us from mainland Europe.</p>
    <p>At <em>brewcellarhub.example</em> we price-check our products against other online stores and high-street shops, and work hard to keep prices low and attractive, meaning you can enjoy the coffee you <em>buy online</em> without paying high prices.</p>
    <p>If you have any questions please feel free to contact us on <em>+44 (0) 20 7946 0321</em>, or post a comment on our Chatterly page - <em>chatterly.example/brewcellarhub</em></p>
  </div>
</section>

<!-- new arrivals -->
<div class="abs pill" style="top:962px">New arrivals</div>
<div class="abs row" style="top:1036px">
  <div class="product"><div class="ring"><div class="shot" role="img" aria-label="Bag of ground coffee" style="background:linear-gradient(#2a1c14,#6b4a2a 60%,#c59a4a)"></div></div><div class="compare">COMPARE</div><span class="buy">BUY NOW</span></div>
  <div class="product"><div class="ring"><div class="shot" role="img" aria-label="Decorated coffee tin" style="background:linear-gradient(#e8dccb,#cdb89a);width:84px;height:96px"></div></div><div class="compare">COMPARE</div><span class="buy">BUY NOW</span></div>
  <div class="product"><div class="ring active"><div class="shot" role="img" aria-label="Stainless steel stovetop coffee pot" style="background:linear-gradient(90deg,#6e6e6e,#e6e6e6 45%,#8a8a8a)"></div><div class="flag">Automatic pot<br>£69</div></div><div class="compare">COMPARE</div><span class="buy">BUY NOW</span></div>
</div>

<!-- best sellers -->
<div class="abs rule-title" style="top:1314px">Best sellers</div>
<div class="abs row" style="top:1373px">
  <div class="product"><div class="ring"><div class="shot" role="img" aria-label="Blue bag of coffee beans" style="background:linear-gradient(#1a2546,#2f4680 60%,#b33)"></div></div><div class="compare">COMPARE</div><span class="buy">BUY NOW</span></div>
  <div class="product"><div class="ring"><div class="shot" role="img" aria-label="Red espresso machine" style="background:linear-gradient(#d9382a,#9e2a20);width:92px;height:86px"></div></div><div class="compare">COMPARE</div><span class="buy">BUY NOW</span></div>
  <div class="product"><div class="ring"><div class="shot" role="img" aria-label="Stovetop moka pot" style="background:linear-gradient(90deg,#5e5e5e,#dedede 45%,#7a7a7a)"></div></div><div class="compare">COMPARE</div><span class="buy">BUY NOW</span></div>
</div>

<!-- hot price -->
<div class="abs rule-title" style="top:1635px">Hot price</div>
<div class="abs row" style="top:1694px">
  <div class="product"><div class="badge">-45%</div><div class="ring"><div class="shot" role="img" aria-label="Steel coffee pot" style="background:linear-gradient(90deg,#666,#e4e4e4 45%,#888)"></div></div><div class="compare">COMPARE</div><span class="buy">BUY NOW</span></div>
  <div class="product"><div class="badge">-25%</div><div class="ring"><div class="shot" role="img" aria-label="Blue packet of coffee" style="background:linear-gradient(#24428f,#4f77c9 60%,#1b2e63)"></div></div><div class="compare">COMPARE</div><span class="buy">BUY NOW</span></div>
  <div class="product"><div class="badge">-15%</div><div class="ring"><div class="shot" role="img" aria-label="Capsule coffee machine" style="background:linear-gradient(#2e6fae,#1c1c1c 55%,#555);width:84px;height:96px"></div></div><div class="compare">COMPARE</div><span class="buy">BUY NOW</span></div>
</div>

<!-- help panel -->
<div class="abs help"></div>
<div class="abs pill" style="top:1950px;font-size:14px;letter-spacing:.6px">Got a question? &nbsp;Call us 020 7946 0321</div>

<div class="abs columns">
  <div class="col">
    <div class="col-head">
      <svg width="30" height="24" viewBox="0 0 30 24"><path d="M1 3h5l4 13h15l3-10H8" fill="none" stroke="#999" stroke-width="2.2"/><circle cx="12" cy="21" r="2" fill="#999"/><circle cx="23" cy="21" r="2" fill="#999"/></svg>
      <h3>Shopping<br>with us</h3>
    </div>
    <p>Browse our range, add items to your basket and check out in a few steps. Orders placed before noon leave our store the same day, packed with care and tracked to your door.</p>
    <span class="read">Read more here</span>
  </div>
  <div class="col">
    <div class="col-head">
      <svg width="26" height="26" viewBox="0 0 26 26"><circle cx="13" cy="13" r="11" fill="none" stroke="#999" stroke-width="2.2"/></svg>
      <h3>About<br>brewcellarhub</h3>
    </div>
    <p>We are a small team of coffee lovers sourcing hard to find brands from across Europe. Every product is chosen for taste and quality, so you can enjoy the coffee you love at home.</p>
    <span class="read">Read more here</span>
  </div>
  <div class="col">
    <div class="col-head">
      <svg width="26" height="26" viewBox="0 0 26 26"><path d="M4 4l18 18M22 4L4 22" stroke="#999" stroke-width="3" stroke-linecap="round"/></svg>
      <h3>Technical<br>Support</h3>
    </div>
    <p>Need help with a machine or grinder? Our support team can guide you through setup, cleaning and repairs, and help you find the right spare parts for your model.</p>
    <span class="read">Read more here</span>
  </div>
</div>

<div class="abs pill" style="top:2298px">Worldwide delivery + payment methods</div>

<div class="abs delivery">
  <div class="block">
    <div class="col-head" style="display:flex;gap:10px">
      <svg width="30" height="24" viewBox="0 0 30 24"><path d="M1 12L29 1 20 23 14 15z" fill="#aaa"/></svg>
      <h3>Outside the UK?<br>No problem...</h3>
    </div>
    <p>We ship to Ireland and mainland Europe at low rates. Choose your country at checkout to see delivery costs and times, and track every parcel online until it arrives.</p>
  </div>
  <div class="courier" role="img" aria-label="Photo of a courier holding a parcel"></div>
  <div class="block">
    <div class="col-head" style="display:flex;gap:10px">
      <svg width="30" height="22" viewBox="0 0 30 22"><rect x="1" y="1" width="28" height="20" rx="3" fill="#aaa"/><rect x="1" y="6" width="28" height="4" fill="#fff"/></svg>
      <h3>Pay quickly<br>&amp; easily</h3>
    </div>
    <div class="cards">
      <span>Cardova</span><span>Meridcard</span><span>PayNimbus</span>
      <span>Cardova</span><span>Meridcard</span><span>Vextora</span>
    </div>
  </div>
</div>

<!-- footer -->
<div class="abs foot-logo"><span class="mark"></span><span class="name">brewcellarhub.example</span></div>
<div class="abs foot-cols">
  <div><h4>User options</h4><ul><li>Basket (3)</li><li>My account</li><li>Gift list</li><li>Logout</li></ul></div>
  <div><h4>Main menu</h4><ul><li>Coffee</li><li>Machines</li><li>Accessories</li><li>Other drinks</li><li>Goodies</li></ul></div>
  <div><h4>Company</h4><ul><li>About brewcellarhub</li><li>Contacts</li><li>Legals &amp; policy</li></ul></div>
  <div><h4>More options</h4><ul><li>Delivery worldwide</li><li>How to order</li><li>FAQ</li><li>Help</li><li>Sitemap</li></ul></div>
</div>
<div class="abs join">JOIN US</div>
<div class="abs join-icons" aria-label="chirpwave, Chatterly, Snapframe and Boardnook links"><span></span><span></span><span></span><span></span></div>
<div class="abs seal" role="img" aria-label="Secure payment seal"></div>

<div class="abs strip"></div>
<div class="abs copy">brewcellarhub &nbsp;|&nbsp; Copyright © 2014. All rights reserved.</div>

</body>
</html>
```